Independent Financial Advisor Billboard Campaign - Granite Bridge Financial

I am a local, independent financial advisor. My company is Granite Bridge Financial, located in Charleston, WV. My main source of revenue comes from those nearing or entering retirement that need assistance with financial planning and investment management. Many are looking to rollover their employer retirement plan into an IRA account. I would like a billboard design campaign that focuses on this type of client. Please see our website www.granitebridgefinancial-example.com for more information.

```html
<!DOCTYPE html>
<html lang="en">
<head>
<meta charset="utf-8">
<title>Granite Bridge Financial – Retirement Billboard</title>
<link href="https://fonts.googleapis.com/css2?family=Raleway:ital,wght@0,500;0,600;0,700;0,800;1,800&display=swap" rel="stylesheet">
<style>
  :root{
    --navy:#1b3f73;
    --green:#9bd60f;
    --green-dark:#7cb518;
    --mist:#e4e7ec;
    --white:#ffffff;
    --ink:#1c2c45;
    --stage:#d9d9d9;
  }
  *{margin:0;padding:0;box-sizing:border-box}
  html,body{width:1096px;height:1200px;overflow:hidden}
  body{
    background:radial-gradient(ellipse at 50% 50%,#ececec 0%,var(--stage) 75%);
    font-family:"Raleway",sans-serif;
    position:relative;
  }
  .billboard-frame{
    position:absolute;left:48px;top:415px;width:1000px;height:370px;
    box-shadow:0 22px 28px -14px rgba(0,0,0,.35);
  }
  .billboard{
    position:absolute;left:0;top:0;width:1548px;height:572px;
    transform:scale(.646);transform-origin:0 0;
    background:var(--white);overflow:hidden;
  }
  .billboard-shapes{position:absolute;inset:0;width:1548px;height:572px}
  .brand{
    position:absolute;left:72px;top:42px;display:flex;align-items:center;gap:18px;
  }
  .brand-mark{width:74px;height:74px;background:var(--navy)}
  .brand-name{
    color:var(--navy);font-weight:700;font-size:38px;line-height:1.05;letter-spacing:1px;
    text-transform:uppercase;
  }
  .headline{position:absolute;left:70px;top:160px;font-weight:800;line-height:1}
  .headline-hope{display:block;color:var(--green);font-size:76px;letter-spacing:-1px}
  .headline-retire{display:block;color:var(--navy);font-size:76px;letter-spacing:-1px;margin-top:4px}
  .headline-plan{
    position:absolute;left:70px;top:300px;color:var(--green);
    font-style:italic;font-weight:800;font-size:50px;
  }
  .services{position:absolute;left:73px;top:364px;display:flex;gap:0}
  .service{display:flex;align-items:center;gap:16px;width:293px}
  .service-icon{width:84px;height:84px;background:var(--navy);display:flex;align-items:center;justify-content:center}
  .service-icon svg{width:62px;height:62px}
  .service-label{color:var(--ink);font-weight:600;font-size:25px;line-height:1.15}
  .contact-band{position:absolute;left:0;top:472px;height:100px;display:flex;align-items:center}
  .contact-phone{
    margin-left:74px;display:flex;align-items:center;gap:14px;
    color:var(--white);font-weight:800;font-size:66px;letter-spacing:-1px;
  }
  .contact-phone svg{width:48px;height:48px}
  .contact-web{margin-left:46px;color:var(--white);font-weight:600;font-size:34px}
</style>
</head>
<body>
  <div class="billboard-frame">
    <div class="billboard">
      <svg class="billboard-shapes" viewBox="0 0 1548 572" xmlns="http://www.w3.org/2000/svg">
        <defs>
          <linearGradient id="band" x1="0" x2="1" y1="0" y2="0">
            <stop offset="0.1" stop-color="#1b3f73"/>
            <stop offset="0.5" stop-color="#5d9a2a"/>
            <stop offset="0.9" stop-color="#9bd60f"/>
          </linearGradient>
          <linearGradient id="couple" x1="0" y1="0" x2="1" y2="1">
            <stop offset="0" stop-color="#e9e3dc"/>
            <stop offset="0.5" stop-color="#e6b7a6"/>
            <stop offset="1" stop-color="#8fc4de"/>
          </linearGradient>
          <linearGradient id="advisor" x1="0" y1="0" x2="0" y2="1">
            <stop offset="0" stop-color="#b8917a"/>
            <stop offset="0.55" stop-color="#d7b09a"/>
            <stop offset="1" stop-color="#2a3a5c"/>
          </linearGradient>
        </defs>
        <!-- faint chevrons -->
        <g fill="var(--mist)">
          <polygon points="820,0 960,0 960,140"/>
          <polygon points="900,0 1000,0 1000,100 960,140 960,60"/>
          <polygon points="1400,0 1548,0 1548,130"/>
          <polygon points="1490,330 1548,270 1548,572 1520,572"/>
        </g>
        <!-- contact band -->
        <polygon points="0,472 1210,472 1310,572 0,572" fill="url(#band)"/>
        <!-- stripes -->
        <polygon points="990,215 1205,0 1235,0 1235,40 1025,250" fill="var(--green)"/>
        <polygon points="1280,0 1320,0 1548,228 1548,268" fill="var(--navy)"/>
        <polygon points="990,355 1030,320 1265,555 1265,572 1225,572" fill="var(--navy)"/>
        <polygon points="1282,572 1548,306 1548,352 1330,572" fill="var(--green)"/>
        <!-- photo areas -->
        <polygon points="1273,22 1538,287 1273,552 1008,287" fill="url(#couple)" role="img" aria-label="Photo of a smiling retired couple embracing"/>
        <polygon points="928,174 1041,287 928,400 815,287" fill="url(#advisor)" role="img" aria-label="Portrait of the financial advisor in a suit"/>
      </svg>

      <div class="brand">
        <div class="brand-mark"></div>
        <div class="brand-name">Granite Bridge<br>Financial</div>
      </div>

      <h1 class="headline">
        <span class="headline-hope">DON'T JUST HOPE</span>
        <span class="headline-retire">FOR RETIREMENT...</span>
      </h1>
      <p class="headline-plan">Plan for it</p>

      <div class="services">
        <div class="service">
          <div class="service-icon">
            <svg viewBox="0 0 64 64" fill="none" stroke="#fff" stroke-width="2.5" stroke-linecap="round" stroke-linejoin="round">
              <path d="M6 26l10-6 10 4 8-4 10 2 14 6"/><path d="M16 20l-8 16M50 22l8 14"/>
              <path d="M22 36l8-8 10 8 8 4-4 4-6-4M30 42l-4 4M36 44l-4 4"/>
              <path d="M26 10v5M32 8v5M38 10v5" stroke="#9bd60f"/>
            </svg>
          </div>
          <div class="service-label">Address<br>Your Needs</div>
        </div>
        <div class="service">
          <div class="service-icon">
            <svg viewBox="0 0 64 64" fill="none" stroke="#fff" stroke-width="2.5" stroke-linecap="round" stroke-linejoin="round">
              <path d="M32 16a12 12 0 0 0-7 22v6h14v-6a12 12 0 0 0-7-22z"/><path d="M26 48h12M28 52h8M32 30v14"/>
              <path d="M32 4v6M14 12l4 4M50 12l-4 4M8 28h6M50 28h6" stroke="#9bd60f"/>
            </svg>
          </div>
          <div class="service-label">Answer Your<br>Questions</div>
        </div>
        <div class="service">
          <div class="service-icon">
            <svg viewBox="0 0 64 64" fill="none" stroke="#fff" stroke-width="2.5" stroke-linejoin="round">
              <rect x="6" y="46" width="6" height="10"/><rect x="16" y="42" width="6" height="14"/><rect x="26" y="38" width="6" height="18"/><rect x="36" y="32" width="6" height="24"/><rect x="46" y="24" width="6" height="32"/>
              <path d="M8 36l16-10 10 4 20-20M46 10h8v8" stroke="#9bd60f" stroke-linecap="round"/>
              <circle cx="22" cy="16" r="7"/>
            </svg>
          </div>
          <div class="service-label">Build<br>a Plan</div>
        </div>
      </div>

      <div class="contact-band">
        <div class="contact-phone">
          <svg viewBox="0 0 48 48" fill="none" stroke="#9bd60f" stroke-width="4" stroke-linecap="round">
            <path d="M14 6l6 9-4 5c2 5 6 9 11 11l5-4 9 6-3 7C24 41 7 24 7 9z" fill="#9bd60f" stroke="none"/>
            <path d="M28 12a9 9 0 0 1 8 8M28 4a17 17 0 0 1 16 16"/>
          </svg>
          <span>304.555.0142</span>
        </div>
        <div class="contact-web">granitebridgefinancial-example.com</div>
      </div>
    </div>
  </div>
</body>
</html>
```